Food Festival "Signature Cocktail" Booth Banner

Need a 3'x9'6" (36" tall x 114" wide) Outdoor Banner for a new "Signature Cocktail" booth at an outdoor food festival. Pellston Onion Jubilee is a non profit festival and the World Record largest Garlic Festival with average of 100K attendees over 3 days. Actual drink served will vary from year to year, but banner for the booth with be reused each year so it will be non drink specific. Banner needs to catch attendee's attention both at a quick glance and from a distance outdoors to drive traffic and sales to the booth. It will be mounted above the sales window of a 10x10 Festival Booth on PVC frame (see attached pic for reference). "Signature Cocktail" is required text along with it being identified as a Pellston Onion Jubilee booth either through use of attached logo (color can be modified) or "Pellston Onion Jubilee" text since we also have for profit competing vendors. Banner will be full color print. Idea concepts: Neon Sign, Art Deco elegant, reclaimed wood...but open to any concepts. Festival website: https://pellstononionjubilee.example

Target Market(s)

Food Festival Attendees

Font styles to use
Decorative
Script
Other font styles liked:
• Neon, heavy weight fonts, open.

Colors

Designer to choose colors to be used in the design.

Requirements
Must have
• "Signature Cocktail" and "Pellston Onion Jubilee" text or POJ Logo provided, colors and layout that stands out and easily identifiable and readable from a long distance with strong text
Nice to have
• Vibrant engaging background,, ties to Garlic
Should not have
• Clip art, generic text

```html
<!DOCTYPE html>
<html lang="en">
<head>
<meta charset="utf-8">
<title>Signature Cocktails – Booth Banner</title>
<link rel="stylesheet" href="https://fonts.googleapis.com/css2?family=Tilt+Neon&family=Neonderthaw&display=swap">
<style>
  :root {
    --page: #ffffff;
    --night: #0b0406;
    --plum-deep: #1e0718;
    --plum-glow: #6a1a6a;
    --marquee: #ffe23a;
    --marquee-glow: #ffb800;
    --neon-white: #fff0ff;
    --neon-pink: #ff3ce0;
    --neon-violet: #e27dff;
    --neon-orange: #ffa646;
    --neon-cyan: #2ee9ff;
  }
  html, body {
    margin: 0;
    width: 1200px;
    height: 1200px;
    overflow: hidden;
    background: var(--page);
  }
  .banner {
    position: absolute;
    left: 50px;
    top: 426px;
    width: 1100px;
    height: 347px;
    box-shadow: 0 0 18px rgba(255, 226, 58, 0.25);
  }
  .banner svg { display: block; }
  .headline {
    font-family: "Tilt Neon", sans-serif;
    fill: none;
    stroke: var(--neon-white);
    stroke-width: 4;
  }
  .script {
    font-family: "Neonderthaw", cursive;
    fill: var(--neon-violet);
    stroke: var(--neon-violet);
    stroke-width: 1.5;
  }
  .festival-name {
    font-family: "Tilt Neon", sans-serif;
    fill: var(--neon-orange);
    letter-spacing: 2px;
  }
</style>
</head>
<body>
  <div class="banner">
    <svg width="1100" height="347" viewBox="0 0 1100 347" xmlns="http://www.w3.org/2000/svg">
      <defs>
        <radialGradient id="backdrop" cx="50%" cy="62%" r="62%">
          <stop offset="0" stop-color="var(--plum-glow)"/>
          <stop offset="0.55" stop-color="var(--plum-deep)"/>
          <stop offset="1" stop-color="var(--night)"/>
        </radialGradient>
        <filter id="glow-pink" x="-20%" y="-40%" width="140%" height="180%">
          <feGaussianBlur stdDeviation="6" result="b"/>
          <feFlood flood-color="#ff3ce0"/>
          <feComposite in2="b" operator="in" result="c"/>
          <feMerge><feMergeNode in="c"/><feMergeNode in="c"/><feMergeNode in="SourceGraphic"/></feMerge>
        </filter>
        <filter id="glow-yellow" x="-5%" y="-10%" width="110%" height="120%">
          <feGaussianBlur stdDeviation="3" result="b"/>
          <feFlood flood-color="#ffb800"/>
          <feComposite in2="b" operator="in" result="c"/>
          <feMerge><feMergeNode in="c"/><feMergeNode in="SourceGraphic"/></feMerge>
        </filter>
        <linearGradient id="glass-left" x1="0" y1="0" x2="1" y2="1">
          <stop offset="0" stop-color="#ff9a3c" stop-opacity="0.55"/>
          <stop offset="1" stop-color="#2ee9ff" stop-opacity="0.55"/>
        </linearGradient>
        <linearGradient id="glass-right" x1="0" y1="0" x2="1" y2="1">
          <stop offset="0" stop-color="#ffe23a" stop-opacity="0.55"/>
          <stop offset="1" stop-color="#2ee9ff" stop-opacity="0.55"/>
        </linearGradient>
      </defs>

      <!-- backdrop -->
      <rect class="backdrop" width="1100" height="347" fill="url(#backdrop)"/>

      <!-- marquee frame -->
      <g class="marquee" filter="url(#glow-yellow)">
        <rect x="19" y="20" width="1062" height="307" rx="16" fill="none" stroke="var(--marquee)" stroke-width="2.5"/>
        <rect x="37" y="39" width="1026" height="269" rx="8" fill="none" stroke="var(--marquee)" stroke-width="9" stroke-linecap="round" stroke-dasharray="0 34"/>
      </g>

      <!-- neon glass, left -->
      <rect x="80" y="138" width="124" height="132" rx="14" fill="url(#glass-left)" role="img" aria-label="Neon outline of a tumbler with ice cubes, a straw and an orange slice"/>
      <!-- neon glass, right -->
      <rect x="884" y="128" width="130" height="150" rx="14" fill="url(#glass-right)" role="img" aria-label="Neon outline of a martini glass with a lemon slice and an olive pick"/>

      <!-- headline -->
      <text class="headline" x="550" y="151" text-anchor="middle" font-size="124" textLength="602" lengthAdjust="spacingAndGlyphs" filter="url(#glow-pink)">SIGNATURE</text>
      <text class="script" x="550" y="246" text-anchor="middle" font-size="128" filter="url(#glow-pink)">Cocktails</text>
      <text class="festival-name" x="550" y="282" text-anchor="middle" font-size="17">PELLSTON ONION JUBILEE</text>
    </svg>
  </div>
</body>
</html>
```